Dale Winfrey Drum Demo

My husband and I just moved to Nashville. Dale (my husband) is a drummer with 30 years of experience. We have a CD that we would like to promote with hope that he can get a gig doing what he loves. We would like your talented artists to create a CD cover and label. We are here to promote Dale, although we also think the rest of the band should be mentioned and recognized. I am going to put the names of the musicians as well as two pictures that can be used for the outside cover if necessary. On the inside of the cover I would like the band members mentioned as well as a little bio. about Dale.
Dale Winfrey - drums and vocals
Mark Bellweather - vocals
Sam Pikeley - bass
Rick Danso - lead guitar

Dale's bio
Born in Massachusetts
30 years experience
some drumming school
local band experience
music played: blues, classic rock, country, jazz, and alternative
influences: Walt Esterby, Lenny Vask, Owen Hask, Hal Dombrovski
Great passion, feel, and desire for music....something which cannot be taught!!!

```html
<!DOCTYPE html>
<html lang="en">
<head>
<meta charset="utf-8">
<title>Dale Winfrey – Demo</title>
<link href="https://fonts.googleapis.com/css2?family=Russo+One&family=Arimo:wght@700&display=swap" rel="stylesheet">
<style>
  :root {
    --paper: #ffffff;
    --ink: #000000;
    --stage-red: #e01008;
    --deep-red: #5a0000;
    --chrome-light: #f4f4f4;
    --chrome-mid: #9a9a9a;
    --chrome-dark: #3c3c3c;
    --title-red: #ff1a0a;
  }
  html, body {
    margin: 0;
    padding: 0;
    width: 1200px;
    height: 1200px;
    overflow: hidden;
    background: var(--paper);
  }
  .cover {
    position: absolute;
    left: 33px;
    top: 33px;
    width: 1125px;
    height: 1128px;
    background: var(--ink);
    overflow: hidden;
  }
  .stage-photo {
    position: absolute;
    left: 0;
    top: 0;
    width: 1125px;
    height: 800px;
    background:
      radial-gradient(ellipse 260px 200px at 1000px 420px, rgba(230,20,10,0.85), transparent 70%),
      radial-gradient(ellipse 320px 260px at 640px 480px, rgba(200,15,8,0.75), transparent 72%),
      radial-gradient(ellipse 360px 90px at 330px 60px, rgba(224,16,8,0.9), transparent 75%),
      radial-gradient(ellipse 200px 120px at 1000px 60px, rgba(224,16,8,0.8), transparent 75%),
      radial-gradient(ellipse 240px 60px at 300px 580px, rgba(160,10,5,0.7), transparent 75%),
      linear-gradient(180deg, rgba(0,0,0,0) 60%, var(--ink) 100%),
      linear-gradient(90deg, var(--ink) 0%, #1a0000 40%, var(--deep-red) 100%);
  }
  .artist-name {
    position: absolute;
    left: 27px;
    top: 842px;
    margin: 0;
    font-family: "Russo One", sans-serif;
    font-weight: 400;
    font-size: 116px;
    line-height: 1;
    letter-spacing: 1px;
    white-space: nowrap;
    background: linear-gradient(180deg, var(--chrome-light) 0%, #d8d8d8 35%, var(--chrome-dark) 52%, var(--chrome-mid) 70%, var(--chrome-light) 100%);
    -webkit-background-clip: text;
    background-clip: text;
    color: transparent;
  }
  .release-type {
    position: absolute;
    left: 1043px;
    top: 919px;
    margin: 0;
    font-family: "Arimo", sans-serif;
    font-weight: 700;
    font-size: 140px;
    line-height: 1;
    color: var(--title-red);
    white-space: nowrap;
    transform: translate(-50%, -50%) rotate(-90deg);
  }
</style>
</head>
<body>
  <main class="cover">
    <div class="stage-photo" role="img" aria-label="Drum kit, cymbals, amplifier and electric guitar on a stage bathed in red light"></div>
    <h1 class="artist-name">Dale Winfrey</h1>
    <p class="release-type">Demo</p>
  </main>
</body>
</html>
```